We would like to incorporate our logo into letterhead design and envelopes. We are looking for something that is moderately conservative but not old law firm style. Both the envelopes and the letterhead must have both firm addresses. We would like to incorporate the color of the logo, but only a small amount of color - perhaps on one of the borders. The addresses for the firm locations are listed below. Given that it is a law firm, it needs to somewhat conservative, but not the old school, small black font on cream colored paper design.

The firm addresses are:

27815 N. Harlow Pemberton Pkwy.
Ste 4200
Scottsdale, AZ 85391

6100 W. Cedar Avenue
Ste 700
Burbank, CA 91623

Industry/Entity Type

Legal

Colors

Designer to choose colors to be used in the design.

Requirements
Must have
• Both addresses:
• 27815 N. Harlow Pemberton Pkwy.
• Ste 4200
• Scottsdale, AZ 85391
• 6100 W. Cedar Avenue
• Ste 700
• Burbank, CA 91623
Nice to have
• Small amount of color on border(s) that matches the logo but not too much color

```html
<!DOCTYPE html>
<html lang="en">
<head>
<meta charset="utf-8">
<title>Devane Law – Stationery</title>
<link rel="stylesheet" href="https://fonts.googleapis.com/css2?family=Marcellus&family=Open+Sans:ital,wght@1,500&family=Verdana&display=swap">
<style>
  :root {
    --ink: #29235f;
    --paper: #f4f4f4;
    --canvas: #ffffff;
    --text: #1f1f1f;
    --title: #163c4a;
    --rule: #6f6a95;
    --shadow: rgba(0, 0, 0, 0.45);
  }
  * { box-sizing: border-box; margin: 0; padding: 0; }
  html, body {
    width: 1200px; height: 834px; overflow: hidden;
    background: var(--canvas);
  }
  .board { position: relative; width: 1200px; height: 834px; }
  .board-title {
    position: absolute; left: 0; right: 0; top: 31px;
    text-align: center;
    font: 20px Verdana, "Open Sans", sans-serif;
    color: var(--title);
  }
  .sheet {
    position: absolute;
    background: var(--paper);
    box-shadow: 3px 3px 5px var(--shadow);
    overflow: hidden;
  }
  .sheet .edge-art { position: absolute; left: 0; top: 0; }
  .firm-name {
    position: absolute; left: 0; right: 0;
    text-align: center;
    font-family: "Marcellus", serif;
    font-weight: 400;
    color: var(--ink);
    line-height: 1;
    white-space: nowrap;
  }
  .header-rule {
    position: absolute; height: 1px; background: var(--rule);
  }
  .address {
    position: absolute;
    font-family: "Open Sans", sans-serif;
    font-style: italic; font-weight: 500;
    color: var(--text);
    text-align: center;
    line-height: 1.2;
    white-space: nowrap;
  }

  /* Letterhead */
  .letterhead { left: 26px; top: 90px; width: 550px; height: 711px; }
  .letterhead .firm-name { top: 24px; font-size: 72px; letter-spacing: 1px; }
  .letterhead .header-rule { left: 39px; width: 471px; top: 83px; }
  .letterhead .address { top: 91px; font-size: 9.5px; }
  .letterhead .address-az { left: 40px; }
  .letterhead .address-ca { left: 338px; }

  /* Envelope front */
  .envelope-front { left: 596px; top: 101px; width: 574px; height: 288px; }
  .envelope-front .firm-name { top: 21px; font-size: 57px; letter-spacing: 1px; }
  .envelope-front .header-rule { left: 96px; width: 380px; top: 68px; }
  .envelope-front .address { top: 73px; font-size: 7.5px; }
  .envelope-front .address-az { left: 97px; }
  .envelope-front .address-ca { left: 333px; }

  /* Envelope back */
  .envelope-back { left: 596px; top: 499px; width: 574px; height: 287px; }
  .envelope-back .firm-name { top: 115px; font-size: 57px; letter-spacing: 1px; }
  .envelope-back .header-rule { left: 96px; width: 380px; top: 164px; }
</style>
</head>
<body>
<main class="board">
  <h1 class="board-title">Law Firm Stationary Design</h1>

  <section class="sheet letterhead" aria-label="Letterhead">
    <svg class="edge-art" width="550" height="711" viewBox="0 0 550 711" aria-hidden="true">
      <rect x="0" y="0" width="6" height="711" fill="var(--ink)"/>
      <polygon points="0,649 6,649 38,711 0,711" fill="var(--ink)"/>
    </svg>
    <div class="firm-name">DEVANE LAW</div>
    <div class="header-rule"></div>
    <p class="address address-az">27815 N. Harlow Pemberton Pkwy. Ste 4200, Scottsdale,<br>AZ 85391</p>
    <p class="address address-ca">6100 W. Cedar Avenue Ste 700, Burbank,<br>CA 91623</p>
  </section>

  <section class="sheet envelope-front" aria-label="Envelope front">
    <svg class="edge-art" width="574" height="288" viewBox="0 0 574 288" aria-hidden="true">
      <rect x="0" y="0" width="4" height="288" fill="var(--ink)"/>
      <polygon points="0,237 4,237 30,288 0,288" fill="var(--ink)"/>
    </svg>
    <div class="firm-name">DEVANE LAW</div>
    <div class="header-rule"></div>
    <p class="address address-az">27815 N. Harlow Pemberton Pkwy. Ste 4200, Scottsdale,<br>AZ 85391</p>
    <p class="address address-ca">6100 W. Cedar Avenue Ste 700, Burbank,<br>CA 91623</p>
  </section>

  <section class="sheet envelope-back" aria-label="Envelope back">
    <svg class="edge-art" width="574" height="287" viewBox="0 0 574 287" aria-hidden="true">
      <path d="M0,0 H574 V18 Q560,22 548,40 Q542,54 525,54 H40 Q26,54 20,40 L0,0 Z" fill="var(--ink)"/>
    </svg>
    <div class="firm-name">DEVANE LAW</div>
    <div class="header-rule"></div>
  </section>
</main>
</body>
</html>
```